Re-Design Of High Traffic Content Hub

“Tarmac Compass, is a comprehensive online hub dedicated to helping over 150,000 visitors a month have a smooth towing trip. Tarmac Compass is the place where you’ll find up-to-date information, practical advice, ‘how to’ guides and handy tips for your caravan, trailer and anything else you need to tow."

Content on the site is split in to 4 main pillars:
“Caravan” “Trailer” “Boating” "Travel"

Each pillar is split further in to 3 categories:
How To • Products • Reviews

We are crowd-sourcing the redesign of the following pages:

- Home Page
- Category Page
- Single Post
- Search Results
- Static Content Page (Terms & Conditions/ About / Privacy Policy)

Look and feel to be implemented inline with UX best practice.
A strong conversion focus is desirable site wide (e-book downloads & newsletter subscriptions are offered).

Our preference is for the home page to provide the visitor with a visual snapshot of fresh site content and encourage the user to explore the site further using navigation or search.

Design elements to be featured on the home page:
Main Navigation
Site Search
Newsletter Subscription Box
eBook Download CTA
Mission Statement
2 x Recent articles from each top level content pillar including featured image and title.
An area to feature 3 of the site's best performing articles including featured image, title and excerpt.

Mission Statement: "Tarmac Compass is the place you can turn to for up-to-date information, practical advice, ‘how to’ guides and handy tips for your caravan, trailer and anything else worth towing. "

Selected designs will be coded in responsive bootstrap so preference will be given to designs presented with this in mind.

Logo's attached in transparent white and transparent dark.

Live site located at www.tarmaccompass-demo.com.au

ec1f27
f5f5f5
b2b2b2
ffffff

• Strong conversion focus (eBook downloads and newsletter subscriptions)

```html
<!DOCTYPE html>
<html lang="en">
<head>
<meta charset="utf-8">
<title>Tarmac Compass – Home</title>
<link rel="stylesheet" href="https://fonts.googleapis.com/css2?family=Oswald:wght@400;500&family=Open+Sans:ital,wght@0,400;0,600;1,400&display=swap">
<style>
:root{
  --red:#ec1f27;
  --deep-red:#8e1216;
  --light:#f5f5f5;
  --grey:#b2b2b2;
  --white:#ffffff;
  --asphalt:#262626;
  --panel:#3d3d3d;
  --panel-dark:#1c1c1c;
  --yellow:#f4c20d;
  --orange:#f29a1f;
}
*{box-sizing:border-box;margin:0;padding:0}
html,body{width:953px;height:1200px;overflow:hidden}
body{position:relative;background:radial-gradient(circle at 50% 40%,#333 0%,var(--asphalt) 70%);font-family:"Open Sans",Arial,sans-serif;color:var(--white)}
.abs{position:absolute}
.head-font{font-family:"Oswald","Arial Narrow",sans-serif;font-weight:500}

/* top bar */
.social-bar{left:702px;top:0;width:251px;height:26px;background:var(--red);clip-path:polygon(12px 0,100% 0,100% 100%,0 100%);display:flex;gap:11px;align-items:center;padding-left:30px}
.social-bar span{width:15px;height:15px;background:#3a0a0b;border-radius:2px}

/* brand */
.brand-name{left:94px;top:34px;font-size:29px;line-height:28px;letter-spacing:.5px}
.sponsor{left:204px;top:0;width:62px;height:94px;background:var(--red);text-align:center;padding-top:60px}
.sponsor small{display:block;font-size:5px;letter-spacing:.3px;margin-bottom:3px}
.sponsor b{font-family:"Oswald",sans-serif;font-weight:500;font-size:12px}

/* nav */
.main-nav{left:354px;top:66px;display:flex;align-items:center;height:40px}
.main-nav a{font-size:19px;color:var(--white);text-decoration:none;margin-right:14px}
.main-nav a.active{background:var(--white);color:var(--red);padding:4px 14px 4px 18px;clip-path:polygon(10px 0,100% 0,100% 100%,0 100%);margin-right:20px}
.sub-nav{left:426px;top:106px;width:228px;height:19px;background:var(--white);color:#111;font-size:10px;font-weight:600;display:flex;justify-content:center;align-items:center;gap:12px;z-index:3}
.search{left:678px;top:68px;width:190px;height:26px;background:#8c8c8c;clip-path:polygon(8px 0,100% 0,100% 100%,0 100%);font-size:10px;color:#eee;padding:6px 20px;letter-spacing:.5px}

/* hero */
.hero{left:0;top:106px;width:953px;height:282px}
.hero-caption{left:78px;top:210px;width:210px;height:162px;background:rgba(20,20,20,.85);padding:16px 12px}
.hero-caption h2{color:var(--yellow);font-size:18px;margin-bottom:10px}
.hero-caption p{font-size:12px;line-height:18px;text-align:justify}
.hero-side-title{left:598px;top:340px;width:355px;text-align:center;font-size:18px}
.dots{display:flex;gap:3px}
.dots i{width:7px;height:7px;background:var(--white)}
.dots i:first-child{background:var(--red);outline:1px solid var(--white)}

/* content sheet */
.sheet{left:79px;top:390px;width:793px;height:698px;background:var(--white)}
.feature{left:85px;top:396px;width:462px;height:288px}
.feature-text{left:100px;top:520px;width:150px}
.feature-text h3{color:var(--yellow);font-size:19px;line-height:28px;margin-bottom:20px}
.feature-text p{font-size:11.5px;line-height:18px;text-align:justify;width:186px}

.ebook{left:553px;top:396px;width:312px;height:288px;background:var(--panel)}
.panel-head{background:var(--panel-dark);font-family:"Oswald",sans-serif;font-weight:500;color:var(--white)}
.ebook .panel-head{height:58px;font-size:21px;display:flex;align-items:center;justify-content:center;gap:12px}
.phone-badge{width:38px;height:38px;border-radius:50%;background:var(--yellow);display:flex;align-items:center;justify-content:center}
.ebook p{font-style:italic;font-size:14.5px;line-height:22px;text-align:justify;padding:12px 24px 0 24px}
.email{background:var(--white);color:#222;font-style:italic;font-size:14px;padding:7px 8px}
.ebook .email{position:absolute;left:23px;top:190px;width:266px;height:33px}
.ebook-cta{position:absolute;left:24px;top:240px;display:flex;align-items:center;gap:18px;color:var(--yellow);font-size:19px}

.popular{left:85px;top:690px;width:313px;height:288px;background:var(--panel)}
.tabs{height:38px;display:flex;font-size:19px}
.tabs .on{width:160px;background:var(--panel-dark);color:var(--yellow);padding:5px 16px;clip-path:polygon(0 0,100% 0,88% 100%,0 100%)}
.tabs .off{flex:1;text-align:right;padding:5px 14px;color:var(--light)}
.popular ul{list-style:none;padding:0 10px}
.popular li{height:53px;display:flex;align-items:center;font-size:14.5px;border-bottom:1px solid #2c2c2c;white-space:nowrap;overflow:hidden}
.popular li::before{content:"";width:7px;height:7px;background:var(--red);outline:1px solid var(--light);margin:0 10px 0 0;flex:none}

.pillars{left:404px;top:690px;width:461px;height:130px;background:var(--panel);display:flex}
.pillar{width:115px;text-align:center;padding-top:12px;font-size:19px;color:#c9c9c9}
.pillar.active{background:var(--deep-red);color:var(--yellow)}
.pillar svg{display:block;margin:10px auto 0}

.newsletter{left:404px;top:826px;width:461px;height:152px;background:var(--panel)}
.newsletter .panel-head{height:40px;font-size:20px;padding:6px 14px}
.newsletter p{font-style:italic;font-size:11.5px;line-height:17px;padding:6px 14px;text-align:justify}
.newsletter .email{position:absolute;left:14px;top:110px;width:266px;height:31px}
.submit{position:absolute;left:298px;top:110px;width:151px;height:31px;background:var(--deep-red);color:var(--yellow);font-size:18px;text-align:center;line-height:31px}

.mission{left:84px;top:990px;width:306px;color:#111}
.mission h4,.tags h4{font-size:21px;font-weight:400;font-family:"Oswald",sans-serif;margin-bottom:4px}
.mission p{font-style:italic;font-size:11.5px;line-height:17px;text-align:justify}
.tags{left:406px;top:990px;color:#111;font-size:11.5px;line-height:17px}
.tags em{font-style:normal;color:var(--deep-red)}
.partner{left:688px;top:1010px;text-align:center;color:var(--red)}
.partner b{font-family:"Oswald",sans-serif;font-weight:500;font-size:40px;line-height:40px;display:block}
.partner span{color:var(--grey);font-family:"Oswald",sans-serif;font-size:13px;letter-spacing:1px}

.sheet-shadow{left:140px;top:1088px;width:680px;height:22px;background:radial-gradient(ellipse at 50% 0,rgba(0,0,0,.7),transparent 70%)}
.footer-links{left:0;top:1138px;width:953px;text-align:center;font-size:11px;font-weight:600;letter-spacing:.3px}
.footer-links span{margin:0 10px}
.base-line{left:0;top:1194px;width:953px;height:6px;background:var(--red)}
</style>
</head>
<body>

<div class="abs social-bar" aria-label="Social links"><span></span><span></span><span></span><span></span><span></span></div>

<div class="abs brand-name head-font">TARMAC<br>COMPASS</div>
<div class="abs sponsor"><small>BROUGHT TO YOU BY</small><b>TOWMARK</b></div>

<nav class="abs main-nav head-font">
  <a class="active" href="#">CARAVAN</a><a href="#">TRAILERS</a><a href="#">BOATS</a><a href="#">TRAVEL</a>
</nav>
<div class="abs sub-nav"><span>HOW TO</span>|<span>PRODUCTS</span>|<span>REVIEWS</span></div>
<div class="abs search">SEARCH</div>

<svg class="abs hero" viewBox="0 0 953 282" width="953" height="282">
  <polygon points="0,0 658,0 584,282 0,282" fill="#6b4a32" role="img" aria-label="Photo of a portable generator on red dirt at a bush campsite"/>
  <polygon points="0,0 658,0 584,282 0,282" fill="url(#dirt)"/>
  <polygon points="664,0 953,0 953,282 590,282" fill="url(#park)" role="img" aria-label="Photo of a caravan being hitched to a red car on a grassy park"/>
  <polygon points="603,234 953,234 953,282 590,282" fill="rgba(142,18,22,.88)"/>
  <line x1="661" y1="0" x2="587" y2="282" stroke="#fff" stroke-width="5"/>
  <defs>
    <linearGradient id="dirt" x1="0" y1="0" x2="0" y2="1"><stop offset="0" stop-color="#556b3c" stop-opacity=".6"/><stop offset=".4" stop-color="#8a6446" stop-opacity=".2"/><stop offset="1" stop-color="#5a3b27" stop-opacity=".3"/></linearGradient>
    <linearGradient id="park" x1="0" y1="0" x2="0" y2="1"><stop offset="0" stop-color="#9db4c8"/><stop offset=".45" stop-color="#4d6b3a"/><stop offset="1" stop-color="#7c8a72"/></linearGradient>
  </defs>
</svg>
<div class="abs hero-caption"><h2 class="head-font">How To Use A Generator</h2><p>To generate or not to generate? For the RV traveller who spends long periods of time in remote areas or without mains electricity,</p></div>
<div class="abs hero-side-title head-font">5 Tips For Hitching Up Your Caravan</div>
<div class="abs dots" style="left:486px;top:370px"><i></i><i></i><i></i><i></i></div>

<div class="abs sheet"></div>

<svg class="abs feature" viewBox="0 0 462 288" width="462" height="288">
  <defs><linearGradient id="beach" x1="0" y1="0" x2="0" y2="1"><stop offset="0" stop-color="#8fb0d8"/><stop offset=".55" stop-color="#7d9a6a"/><stop offset=".75" stop-color="#e8e1d2"/><stop offset="1" stop-color="#d7cdb9"/></linearGradient></defs>
  <rect width="462" height="288" fill="url(#beach)" role="img" aria-label="Photo of a sandy north Queensland beach with a bleached tree"/>
  <polygon points="0,0 60,0 250,288 0,288" fill="rgba(142,18,22,.9)"/>
  <g fill="none" stroke="#fff" stroke-width="3"><path d="M22 62 a22 17 0 1 1 10 14 l-10 6 z"/><path d="M36 66 a18 14 0 1 0 38 4"/></g>
  <g fill="#fff"><circle cx="38" cy="71" r="2.5"/><circle cx="47" cy="71" r="2.5"/><circle cx="56" cy="71" r="2.5"/></g>
</svg>
<div class="abs feature-text"><h3 class="head-font">Top 3 North<br>Queensland<br>Campsites</h3><p>Heading North this winter? These three Queensland campsites are our pick of the best.</p></div>
<div class="abs dots" style="left:487px;top:663px"><i></i><i></i><i></i><i></i><i></i></div>

<section class="abs ebook">
  <div class="panel-head">DOWNLOAD OUR FREE E-BOOK
    <span class="phone-badge"><svg width="14" height="22" viewBox="0 0 14 22"><rect x="1" y="1" width="12" height="20" rx="2" fill="#fff" stroke="#c43" stroke-width="1.5"/><rect x="3" y="4" width="8" height="12" fill="#ec1f27"/></svg></span>
  </div>
  <p>Our towing e-book, packed full of essential safety, preparation and towing tips will be the perfect driving companion. Receive your free e-book and sign up to our newsletter now!</p>
  <div class="email">Enter your Email Address</div>
  <div class="ebook-cta head-font">DOWNLOAD E-BOOK NOW
    <svg width="44" height="40" viewBox="0 0 44 40"><path d="M4 20 L10 12 H34 L40 20 V36 H4 Z" fill="var(--orange)"/><path d="M4 20 H14 L17 26 H27 L30 20 H40" fill="none" stroke="#fff" stroke-width="2"/><path d="M22 0 V14 M16 9 L22 15 L28 9" stroke="#2f7fd6" stroke-width="4" fill="none"/></svg>
  </div>
</section>

<section class="abs popular">
  <div class="tabs head-font"><div class="on">Most Popular</div><div class="off">Recent</div></div>
  <ul>
    <li>5 Tips For Hitching Up Your Caravan</li>
    <li>How To Stay Snug Whilst Caravanning This..</li>
    <li>How To Theft-Proof Your Caravan</li>
    <li>Continuing to Work Whilst You’re on the …</li>
    <li>Where can you park your caravan?</li>
  </ul>
</section>

<section class="abs pillars head-font">
  <div class="pillar active">CARAVAN
    <svg width="80" height="56" viewBox="0 0 80 56"><path d="M4 10 H54 V42 H4 Z M54 20 H66 L76 32 V42 H54 Z" fill="#fff"/><rect x="10" y="18" width="14" height="10" fill="var(--deep-red)"/><rect x="58" y="24" width="8" height="8" fill="var(--deep-red)"/><circle cx="18" cy="44" r="8" fill="#fff" stroke="var(--deep-red)" stroke-width="3"/><circle cx="62" cy="44" r="8" fill="#fff" stroke="var(--deep-red)" stroke-width="3"/></svg></div>
  <div class="pillar">TRAILER
    <svg width="86" height="56" viewBox="0 0 86 56"><rect x="6" y="10" width="52" height="26" fill="#c9c9c9"/><path d="M58 32 H82" stroke="#c9c9c9" stroke-width="4"/><circle cx="20" cy="42" r="8" fill="#c9c9c9" stroke="#3d3d3d" stroke-width="3"/><circle cx="42" cy="42" r="8" fill="#c9c9c9" stroke="#3d3d3d" stroke-width="3"/></svg></div>
  <div class="pillar">BOATING
    <svg width="70" height="56" viewBox="0 0 70 56"><path d="M26 8 H44 V18 H26 Z M16 18 H54 V30 H16 Z" fill="#c9c9c9"/><path d="M6 30 H64 L54 44 H16 Z" fill="#c9c9c9"/><path d="M4 50 q8 -5 16 0 t16 0 t16 0 t16 0" stroke="#c9c9c9" stroke-width="3" fill="none"/></svg></div>
  <div class="pillar">TRAVEL
    <svg width="70" height="56" viewBox="0 0 70 56"><path d="M34 18 Q40 36 30 52" stroke="#c9c9c9" stroke-width="5" fill="none"/><path d="M34 18 Q20 6 8 14 Q22 12 34 18 Q48 4 62 12 Q46 10 34 18 Q40 24 50 34 Q38 20 34 18 Q24 24 16 36 Q26 22 34 18Z" fill="#c9c9c9"/><path d="M8 54 Q34 44 62 54" stroke="#c9c9c9" stroke-width="3" fill="none"/></svg></div>
</section>

<section class="abs newsletter">
  <div class="panel-head">FREE WEEKLY NEWSLETTERS</div>
  <p>Tarmac Compass is the place you can turn to for up-to-date information, practical advice, ‘how to’ guides and handy tips for your caravan, trailer and anything else worth towing. To receive regular towing hints, tips sign up to our newsletter today!</p>
  <div class="email">Enter your Email Address</div>
  <div class="submit head-font">SUBMIT</div>
</section>

<div class="abs mission"><h4>Our Mission</h4><p>Tarmac Compass is the place you can turn to for up-to-date information, practical advice, ‘how to’ guides and handy tips for your caravan, trailer and anything else worth towing.</p></div>
<div class="abs tags"><h4>Tags</h4>Caravan Safe , <em>Replace Trailer Lights</em><br>Caravan TV Antenna , Master Head Lights<br>Manual VS Auto</div>
<div class="abs partner"><b>TOWMARK</b><span>BUILT TO TOW</span></div>

<div class="abs sheet-shadow"></div>
<div class="abs footer-links">TERMS &amp; CONDITIONS<span>|</span>ABOUT TARMAC COMPASS<span>|</span>PRIVACY POLICY</div>
<div class="abs base-line"></div>

</body>
</html>
```